Tovrimel Complete Stationery - Logo already designed

I already have the logo designed see attached. I need have a full set of stationary and business card designed for printing. I have attached an example of what I mean.

Please feel free to be creative. Also you can use the X in the logo by its self if you think it will work.

My details:

Name: Dorian Pelsett
Social media handles: @dorianpelsett
W: dorianpelsett.com
E: info@dorianpelsett.com
​P: 08 7349 5286
PO Box 3872, Wendlemore 6047
ABN 83 274 908 615

Target Market(s)

Anyone looking to be inspired.

Industry/Entity Type

Business

Font styles to use
Sans Serif

Colors
fbee3e
000000

Requirements
Must have
• My details:
• Name: Dorian Pelsett
• Social media handles: @dorianpelsett
• W: dorianpelsett.com
• E: info@dorianpelsett.com
• ​P: 08 7349 5286
• PO Box 3872, Wendlemore 6047
• ABN 83 274 908 615
Nice to have
• Something a little different
Should not have
• must not look tacky.

```html
<!DOCTYPE html>
<html lang="en">
<head>
<meta charset="utf-8">
<title>Tovrimel Business Card</title>
<link rel="stylesheet" href="https://fonts.googleapis.com/css2?family=Oswald:wght@600;700&family=Source+Sans+3:wght@400;700&display=swap">
<style>
  :root {
    --gold: #dbb00c;
    --ink: #1e1e1e;
    --text: #3a3a3a;
    --card: #f4f4f4;
    --backdrop: #9a9a9a;
    --white: #ffffff;
  }
  * { margin: 0; padding: 0; box-sizing: border-box; }
  html, body {
    width: 1105px;
    height: 1200px;
    overflow: hidden;
    background: var(--backdrop);
  }
  .sheet { position: relative; width: 1105px; height: 1200px; }
  .card {
    position: absolute;
    left: 102px;
    width: 900px;
    height: 516px;
    background: var(--card);
    overflow: hidden;
    font-family: "Source Sans 3", sans-serif;
    color: var(--text);
  }
  .card--front { top: 56px; }
  .card--back { top: 628px; }

  .brand-name {
    position: absolute;
    font-family: "Oswald", sans-serif;
    font-weight: 700;
    font-size: 72px;
    line-height: 1;
    color: var(--ink);
    letter-spacing: -1px;
  }
  .card--front .brand-name { right: 52px; top: 70px; }

  .holder-name {
    position: absolute;
    left: 53px;
    top: 282px;
    font-family: "Oswald", sans-serif;
    font-weight: 600;
    font-size: 33px;
    color: var(--ink);
    text-transform: uppercase;
    letter-spacing: 0.5px;
  }
  .divider {
    position: absolute;
    left: 53px;
    right: 52px;
    top: 337px;
    height: 2px;
    background: var(--ink);
  }
  .contact {
    position: absolute;
    top: 352px;
    font-size: 25px;
    line-height: 35px;
  }
  .contact--left { left: 53px; }
  .contact--right { right: 52px; text-align: right; }
  .contact-row { display: flex; align-items: center; gap: 12px; }
  .contact-row svg { width: 20px; height: 20px; fill: var(--ink); }

  .footer-band { position: absolute; left: 0; bottom: 0; width: 900px; height: 42px; }
  .web-address {
    position: absolute;
    right: 52px;
    bottom: 6px;
    font-weight: 700;
    font-size: 27px;
    color: var(--white);
  }
  .web-address .accent { color: var(--gold); }

  .brand-block {
    position: absolute;
    left: 40px;
    top: 48px;
    width: 420px;
    height: 420px;
    background: var(--gold);
  }
  .card--back .brand-name { left: 560px; top: 170px; }
  .social-dots {
    position: absolute;
    left: 638px;
    top: 296px;
    display: flex;
    gap: 6px;
  }
  .social-dots span {
    width: 44px;
    height: 44px;
    border-radius: 50%;
    background: var(--gold);
  }
  .handle {
    position: absolute;
    left: 560px;
    width: 250px;
    top: 344px;
    text-align: center;
    font-size: 24px;
  }
</style>
</head>
<body>
<main class="sheet">
  <section class="card card--front">
    <div class="brand-name">Tovrimel</div>
    <div class="holder-name">Dorian Pelsett</div>
    <div class="divider"></div>
    <div class="contact contact--left">
      <div class="contact-row">
        <svg viewBox="0 0 24 24" aria-hidden="true"><path d="M6.6 10.8a15.1 15.1 0 0 0 6.6 6.6l2.2-2.2a1 1 0 0 1 1-.25 11.4 11.4 0 0 0 3.6.57 1 1 0 0 1 1 1V20a1 1 0 0 1-1 1A17 17 0 0 1 3 4a1 1 0 0 1 1-1h3.5a1 1 0 0 1 1 1c0 1.25.2 2.45.57 3.57a1 1 0 0 1-.25 1z"/></svg>
        <span>08 7349 5286</span>
      </div>
      <div class="contact-row">
        <svg viewBox="0 0 24 24" aria-hidden="true"><path d="M2 5h20v14H2z M2 5l10 8 10-8" fill="var(--ink)"/><path d="M3 6l9 7 9-7" fill="none" stroke="var(--card)" stroke-width="1.6"/></svg>
        <span>info@dorianpelsett.com</span>
      </div>
    </div>
    <div class="contact contact--right">
      <div>ABN 83 274 908 615</div>
      <div>PO Box 3872, Wendlemore 6047</div>
    </div>
    <svg class="footer-band" viewBox="0 0 900 42" aria-hidden="true">
      <rect x="0" y="7" width="510" height="10" fill="var(--gold)"/>
      <polygon points="510,0 900,0 900,42 470,42" fill="var(--ink)"/>
    </svg>
    <div class="web-address">www.<span class="accent">dorianpelsett</span>.com</div>
  </section>

  <section class="card card--back">
    <div class="brand-block"></div>
    <div class="brand-name">Tovrimel</div>
    <div class="social-dots"><span></span><span></span><span></span></div>
    <div class="handle">@dorianpelsett</div>
  </section>
</main>
</body>
</html>
```